Brackley Yard Services Flyer Design

I need a new flyer design for my business, Brackley Yard Services. I’ll be providing my old flyer and logo as references. The new flyer should feature updated wording, contact information, logos, and photos, but still keep the original “What We Do” section and include the phrase “Don’t See? Just Ask!” somewhere near the services. The flyer needs to look great in black and white for door-to-door handouts but also be eye-catching and professional enough for social media use.

The updated content should include the headline “Transforming Outdoor Spaces with Hard Work & Precision” and highlight three main service areas: Landscaping Services (project-based landscaping to clean, prepare, and transform outdoor spaces with precision), Property Cleanup (quick hauls, debris removal, or full cleanouts—no job too big or small), and Ground Preparation (pad preparation, brush removal, and fire lines—making properties safe, functional, and project-ready).

Please also include a “Why Choose Us?” section that lists: Locally owned since 2022, Reliable & affordable – no corners cut, Professional results you can trust, LICENSED AND Insured, and Quality work / on time / references / flexible / follow-up.

At the bottom, include the contact details: Call or Text Today!
www.brackleyyard.example
| sales@brackleyyard.example
| (555) 019-4827

The overall design should be clean, professional, and easy to read with a layout that clearly shows what we offer. Use visuals that represent outdoor services, landscaping, and property cleanup/prep work. I want something that feels trustworthy, family-friendly, and modern.
Use the same photo of leaf clean up from the original flyer if possible.
Our company colors are also black and white. For the most part.

```html
<!DOCTYPE html>
<html lang="en">
<head>
<meta charset="utf-8">
<title>Brackley Yard Services – Built to Work</title>
<link href="https://fonts.googleapis.com/css2?family=Bebas+Neue&family=Oswald:wght@300;400;500;700&family=Barlow+Condensed:ital,wght@0,600;0,700;1,600;1,700&display=swap" rel="stylesheet">
<style>
  :root{
    --ink:#0d0d0d;
    --paper:#ffffff;
    --card:#eeedf1;
    --rule:#1a1a1a;
  }
  *{margin:0;padding:0;box-sizing:border-box}
  html,body{width:927px;height:1200px;overflow:hidden;background:var(--paper)}
  .flyer{position:relative;width:927px;height:1200px;background:var(--paper);color:var(--ink);font-family:'Oswald',sans-serif}

  .hero{position:absolute;left:0;top:0;width:927px;height:337px;background:var(--ink);color:var(--paper);text-align:center}
  .hero__title{position:absolute;left:0;right:0;top:20px;font-family:'Bebas Neue',sans-serif;font-weight:400;font-size:134px;line-height:1;letter-spacing:1px}
  .hero__rule{position:absolute;left:151px;width:624px;height:5px;background:var(--paper)}
  .hero__rule--top{top:150px}
  .hero__rule--bottom{top:223px}
  .hero__tagline{position:absolute;left:0;right:0;top:167px;font-family:'Barlow Condensed',sans-serif;font-style:italic;font-weight:700;font-size:50px;line-height:1;letter-spacing:.5px}
  .hero__intro{position:absolute;left:0;right:0;top:238px;font-weight:400;font-size:16px;line-height:22px;letter-spacing:.3px}
  .hero__intro em{font-style:italic}
  .hero__headline{position:absolute;left:0;right:0;top:286px;font-weight:700;font-size:24px;line-height:32px;letter-spacing:.4px}

  .gallery{position:absolute;left:0;top:349px;width:927px;height:344px}

  .section-title{position:absolute;left:52px;width:824px;top:708px;display:flex;align-items:center;gap:16px}
  .section-title::before,.section-title::after{content:"";flex:1;height:1px;background:var(--rule)}
  .section-title h2{font-family:'Bebas Neue',sans-serif;font-weight:400;font-size:44px;line-height:1;letter-spacing:1px;padding-top:4px}

  .card{position:absolute;background:var(--card);clip-path:polygon(0 0,100% 0,100% calc(100% - 10px),calc(100% - 10px) 100%,0 100%)}
  .tab{position:absolute;height:32px;background:var(--ink);color:var(--paper);font-family:'Barlow Condensed',sans-serif;font-style:italic;font-weight:600;font-size:23px;line-height:32px;text-align:center;white-space:nowrap;letter-spacing:.3px;clip-path:polygon(10px 0,100% 0,100% calc(100% - 10px),calc(100% - 10px) 100%,0 100%,0 10px)}
  .card__text{position:absolute;width:214px;font-weight:300;font-size:14.4px;line-height:18.1px;letter-spacing:-.3px;text-align:justify;hyphens:auto}
  .card__list{position:absolute;font-family:'Barlow Condensed',sans-serif;font-weight:700;font-size:16.5px;line-height:20px;white-space:nowrap}

  .ask{position:absolute;left:320px;width:287px;top:992px;text-align:center;font-family:'Bebas Neue',sans-serif;font-size:34px;line-height:34px;letter-spacing:.5px}
  .brand{position:absolute;left:338px;top:1042px;width:252px;display:flex;align-items:center;gap:12px}
  .brand__mark{width:48px;height:48px;background:var(--ink);flex:none}
  .brand__name{font-weight:700;font-size:25px;line-height:27px;text-transform:uppercase;letter-spacing:.5px}

  .footer-shape{position:absolute;left:0;top:1092px;width:927px;height:94px}
  .cta{position:absolute;left:50px;width:230px;top:1099px;color:var(--paper);font-family:'Barlow Condensed',sans-serif;font-style:italic;font-weight:700;text-align:center}
  .cta__small{display:block;font-size:33px;line-height:34px;letter-spacing:1px}
  .cta__big{display:block;font-size:54px;line-height:48px}
  .contact{position:absolute;left:352px;right:56px;top:1150px;height:26px;display:flex;justify-content:space-between;align-items:center;color:var(--paper);font-size:16.5px;font-weight:400}
  .contact__item{display:flex;align-items:center;gap:7px;white-space:nowrap}
  .contact__item svg{width:20px;height:20px;flex:none}
</style>
</head>
<body>
<main class="flyer">
  <header class="hero">
    <h1 class="hero__title">BUILT TO WORK</h1>
    <div class="hero__rule hero__rule--top"></div>
    <p class="hero__tagline">WE DO GOOD WORK. WE DO HARD WORK</p>
    <div class="hero__rule hero__rule--bottom"></div>
    <p class="hero__intro">Brackley specializes in <em>’the work’</em> too small for big companies too big for the homeowner,<br>or the tasks homeowners just don’t want to do. Nothing is too small or too big for Brackley. Just ask.</p>
    <p class="hero__headline">TRANSFORMING OUTDOOR SPACES WITH HARD WORK &amp; PRECISION</p>
  </header>

  <svg class="gallery" viewBox="0 349 927 344" xmlns="http://www.w3.org/2000/svg">
    <defs>
      <linearGradient id="leaves" x1="0" y1="0" x2="0" y2="1">
        <stop offset="0" stop-color="#c9ced0"/><stop offset=".45" stop-color="#a89a6a"/><stop offset="1" stop-color="#7e5a3d"/>
      </linearGradient>
      <linearGradient id="debris" x1="0" y1="0" x2="0" y2="1">
        <stop offset="0" stop-color="#c9a07a"/><stop offset="1" stop-color="#4d4038"/>
      </linearGradient>
      <linearGradient id="drive" x1="0" y1="0" x2="0" y2="1">
        <stop offset="0" stop-color="#8d96a3"/><stop offset=".55" stop-color="#6f7778"/><stop offset="1" stop-color="#9a948b"/>
      </linearGradient>
    </defs>
    <polygon role="img" aria-label="Photo: rake in fallen autumn leaves beside a row of trees" fill="url(#leaves)" points="2,349 332,349 290,692 2,692"/>
    <polygon role="img" aria-label="Photo: pile of hauled debris, old furniture and carpet" fill="url(#debris)" points="345,349 645,349 605,692 310,692"/>
    <polygon role="img" aria-label="Photo: mini excavator, trailer and plate compactor on a prepared pad" fill="url(#drive)" points="658,349 925,349 925,692 623,692"/>
  </svg>

  <div class="section-title"><h2>WHAT WE DO</h2></div>

  <div class="card" style="left:52px;top:782px;width:235px;height:193px"></div>
  <div class="tab" style="left:65px;top:759px;width:214px">LANDSCAPING SERVICES</div>
  <p class="card__text" style="left:65px;top:801px">Our project-based landscaping services cover everything needed to get your property in shape. We handle yard clean-ups, weed and debris removal, and brush clearing to give your outdoor space a fresh start. From there, we can build it back up with patios, DG, sod, and much more — leaving you with an outdoor space that’s ready to use and enjoy.</p>

  <div class="card" style="left:342px;top:782px;width:242px;height:193px"></div>
  <div class="tab" style="left:355px;top:759px;width:214px">PROPERTY CLEANUP</div>
  <p class="card__text" style="left:355px;top:801px">No matter the size of the job, we’re here to help. From quick hauls and debris removal to complete property cleanouts, we handle it all with efficiency and care. Whether it’s clearing out leftover construction materials, hauling away yard waste, or tackling a full-scale cleanout, our team makes the process simple and stress-free so you can enjoy a clutter-free space.</p>

  <div class="card" style="left:633px;top:782px;width:242px;height:193px"></div>
  <div class="tab" style="left:646px;top:759px;width:214px">GROUND PREPARATION</div>
  <p class="card__text" style="left:646px;top:801px">From pad preparation to brush removal and fire lines, we make sure your property is safe, functional, and ready for any project. Our ground prep services cover everything from clearing unwanted growth to cutting in fire breaks, giving your land the care it needs to stay usable and protected.</p>

  <div class="card" style="left:52px;top:1018px;width:241px;height:74px;clip-path:none"></div>
  <div class="tab" style="left:65px;top:995px;width:214px">LICENSED AND INSURED</div>
  <p class="card__list" style="left:65px;top:1037px">Qualify Work / Hustle / References /<br>On Time / Follow-up</p>

  <p class="ask">DON’T SEE? JUST ASK!</p>
  <div class="brand">
    <span class="brand__mark"></span>
    <span class="brand__name">Brackley Yard<br>Services</span>
  </div>

  <div class="card" style="left:633px;top:1018px;width:242px;height:100px"></div>
  <div class="tab" style="left:641px;top:995px;width:214px">WHY CHOOSE US?</div>
  <p class="card__list" style="left:641px;top:1037px">Locally owned since 2022, Reli-<br>able &amp; affordable – no corners cut,<br>Professional results you can trust.</p>

  <svg class="footer-shape" viewBox="0 1092 927 94" xmlns="http://www.w3.org/2000/svg">
    <polygon fill="var(--ink)" points="0,1092 293,1092 331,1137 927,1137 927,1186 0,1186"/>
  </svg>
  <p class="cta"><span class="cta__small">CALL OR TEXT</span><span class="cta__big">TODAY!</span></p>

  <div class="contact">
    <span class="contact__item">
      <svg viewBox="0 0 24 24" fill="none" stroke="currentColor" stroke-width="1.3"><path d="M6.5 3.5l3 3.5-2 2.2a12 12 0 0 0 7.3 7.3l2.2-2 3.5 3-1.8 2.5C12 19.5 4.5 12 4 5.3z"/><path d="M14 4a6 6 0 0 1 6 6M14 7a3 3 0 0 1 3 3"/></svg>
      (555) 019-4827
    </span>
    <span class="contact__item">
      <svg viewBox="0 0 24 24" fill="none" stroke="currentColor" stroke-width="1.3"><rect x="2.5" y="5.5" width="19" height="13"/><path d="M2.5 5.5l9.5 8 9.5-8"/></svg>
      sales@brackleyyard.example
    </span>
    <span class="contact__item">
      <svg viewBox="0 0 24 24" fill="none" stroke="currentColor" stroke-width="1.3"><circle cx="12" cy="12" r="9.5"/><ellipse cx="12" cy="12" rx="4.2" ry="9.5"/><path d="M2.5 12h19M4 7h16M4 17h16"/></svg>
      www.brackleyyard.example
    </span>
  </div>
</main>
</body>
</html>
```